Riverbend Haven Home Care-Nursing Assessment Form

I am creating a Nursing Assessment Form (which is used to be an intake form for all new patients) for my new home care company, Riverbend Haven Home Care.

It is 15 pages and pretty comprehensive as this is a very regulated field. I have all the necessary content and information attached in the word document below. Now, I am seeking a designer to make it look professional, cohesive and easy to read/ follow.
In order for your Word Document Design to be selected, you must:

1. As mentioned previously, make it easy to read/follow. There should be enough spacing, room to write out all necessary notes, fill out check marks...etc...
2. It should look professional.
3. It should be attractive and eye pleasing. Attached you will find our logo-kindly incorporate it's style into the project as well. The logo should be placed on top of each page.
4. Lastly, we need a Word Document version AND PDF Fillable Option. The fillable PDF should Auto Fill for the Name and Start of Care (SOC) Date.

I have attached a sample form below as well. This is how I envision the finished project to look. Of course, I am open to other suggestions as look as it meets the aforementioned requirements.

Thank you! May the best man or woman win!
Our team looks forward to working with our designer on this project!

Industry/Entity Type

Home Health Care

Font styles to use
Sans Serif

Colors
0255a3
9bcb3c

Requirements
Must have
• Refer to Project Description above.
Nice to have
We must be given a Word Document Option and PDF Fillable Option.

```html
<!DOCTYPE html>
<html lang="en">
<head>
<meta charset="utf-8">
<title>Riverbend Haven Home Care – Initial Assessment Form</title>
<link href="https://fonts.googleapis.com/css2?family=Montserrat:wght@600;700&family=Roboto+Condensed:wght@400;700&display=swap" rel="stylesheet">
<style>
:root{
  --brand-blue:#0255a3;
  --deep-blue:#0b4f96;
  --footer-blue:#003a99;
  --brand-green:#9bcb3c;
  --panel-green:#74c93f;
  --field-green:#d5efc4;
  --ink:#111;
  --paper:#fff;
  --backdrop:#e8edf3;
}
*{margin:0;padding:0;box-sizing:border-box}
html,body{width:1200px;height:728px;overflow:hidden;background:var(--backdrop)}
.canvas{position:relative;width:1200px;height:728px;overflow:hidden}
.page{position:absolute;left:319px;top:0;width:1107px;height:1435px;background:var(--paper);
  transform:scale(.5073);transform-origin:0 0;font-family:"Roboto Condensed",Arial,sans-serif;color:var(--ink);
  box-shadow:0 0 12px rgba(0,0,0,.25)}
.header-band{position:absolute;left:0;top:0;width:1107px;height:116px}
.brand{position:absolute;left:52px;top:52px;display:flex;align-items:center;gap:10px}
.brand-dot{width:26px;height:26px;border-radius:50%;background:var(--brand-green)}
.brand-name{font-family:"Montserrat",Arial,sans-serif;font-weight:700;font-size:17px;line-height:20px;color:var(--brand-blue);width:160px}
.company-tag{position:absolute;left:337px;top:29px;height:27px;padding:0 12px;background:var(--brand-green);
  color:#fff;font-family:"Montserrat",Arial,sans-serif;font-weight:600;font-size:21px;line-height:27px;letter-spacing:.3px}
.form-title{position:absolute;left:333px;top:52px;color:#fff;font-family:"Montserrat",Arial,sans-serif;font-weight:700;font-size:53px;line-height:60px;letter-spacing:.2px}
.t{position:absolute;font-size:15px;line-height:18px;white-space:nowrap}
.b{font-weight:700}
.f{position:absolute;height:19px;background:var(--field-green)}
.cb{position:absolute;width:17px;height:17px;background:var(--field-green)}
.section{position:absolute;left:51px;font-family:"Montserrat",Arial,sans-serif;font-weight:700;font-size:15.5px;line-height:18px;color:var(--brand-blue);letter-spacing:.3px}
.patient-panel{position:absolute;left:51px;top:164px;width:1003px;height:125px;background:var(--panel-green)}
.patient-panel .t{font-weight:700;color:#111}
.wf{position:absolute;height:18px;background:#fff}
.u{text-decoration:underline}
.note-box{position:absolute;left:48px;top:1244px;width:1006px;height:111px;background:var(--field-green)}
.footer-band{position:absolute;left:0;top:1384px;width:1107px;height:51px;background:var(--footer-blue)}
</style>
</head>
<body>
<div class="canvas">
<div class="page">
  <svg class="header-band" viewBox="0 0 1107 116" aria-hidden="true"><polygon points="257,0 1107,0 1107,116 285,116" fill="var(--deep-blue)"/></svg>
  <div class="brand"><span class="brand-dot"></span><span class="brand-name">RIVERBEND HAVEN HOME CARE</span></div>
  <div class="company-tag">RIVERBEND HAVEN HOME CARE</div>
  <div class="form-title">Initial Assessment Form</div>

  <div class="t b" style="left:336px;top:119px">Name :</div><div class="f" style="left:385px;top:118px;width:444px"></div>
  <div class="t b" style="left:836px;top:119px">SOC Date :</div><div class="f" style="left:910px;top:118px;width:145px"></div>

  <div class="patient-panel">
    <div class="t" style="left:15px;top:16px">Patient's Name</div><div class="wf" style="left:115px;top:16px;width:541px"></div>
    <div class="t" style="left:668px;top:16px">Gender</div><div class="wf" style="left:718px;top:16px;width:67px"></div>
    <div class="t" style="left:789px;top:16px">MR#</div><div class="wf" style="left:821px;top:16px;width:66px"></div>
    <div class="t" style="left:891px;top:16px">Date</div><div class="wf" style="left:924px;top:16px;width:70px"></div>
    <div class="t" style="left:15px;top:40px">Primary Diagnosis</div><div class="wf" style="left:136px;top:40px;width:382px"></div>
    <div class="t" style="left:528px;top:40px">Secondary Diagnosis</div><div class="wf" style="left:668px;top:40px;width:326px"></div>
    <div class="t" style="left:15px;top:64px">Other Pertinent Diagnosis</div><div class="wf" style="left:183px;top:64px;width:335px"></div>
    <div class="t" style="left:528px;top:64px">PCP name</div><div class="wf" style="left:668px;top:64px;width:327px"></div>
    <div class="t" style="left:15px;top:88px">Other Physician Name</div><div class="wf" style="left:160px;top:88px;width:357px"></div>
  </div>

  <div class="t b" style="left:51px;top:304px">Prognosis:</div>
  <div class="cb" style="left:144px;top:304px"></div><div class="t" style="left:166px;top:304px">Poor</div>
  <div class="cb" style="left:243px;top:304px"></div><div class="t" style="left:265px;top:304px">Fair</div>
  <div class="cb" style="left:326px;top:304px"></div><div class="t" style="left:348px;top:304px">Good</div>
  <div class="cb" style="left:418px;top:304px"></div><div class="t" style="left:440px;top:304px">Excellent</div>

  <div class="t b" style="left:51px;top:328px">Vital Signs:</div>
  <div class="t" style="left:138px;top:328px">Height:</div><div class="f" style="left:180px;top:328px;width:54px"></div>
  <div class="t" style="left:241px;top:328px">Weight:</div><div class="f" style="left:287px;top:328px;width:89px"></div>
  <div class="t" style="left:384px;top:328px">Temp:</div><div class="f" style="left:427px;top:328px;width:74px"></div>
  <div class="t" style="left:517px;top:328px">Pulse:</div><div class="f" style="left:557px;top:328px;width:79px"></div>
  <div class="t" style="left:656px;top:328px">Resp:</div><div class="f" style="left:694px;top:328px;width:81px"></div>
  <div class="t" style="left:783px;top:328px">B/P:</div><div class="f" style="left:812px;top:328px;width:85px"></div>

  <div class="t b" style="left:51px;top:352px">Allergies:</div><div class="f" style="left:116px;top:352px;width:531px"></div>
  <div class="t b" style="left:51px;top:376px">Past Medical and Surgical History:</div><div class="f" style="left:274px;top:376px;width:782px"></div>

  <div class="section" style="top:416px">SUPPORT SYSTEM :</div>
  <div class="t" style="left:51px;top:441px">Married/Not Married/Single/Divorced/Widowed</div>
  <div class="t" style="left:51px;top:465px">Lives Alone:</div>
  <div class="cb" style="left:142px;top:465px"></div><div class="t" style="left:164px;top:465px">Yes</div>
  <div class="cb" style="left:202px;top:465px"></div><div class="t" style="left:224px;top:465px">No</div>
  <div class="t" style="left:51px;top:489px">Family Composition:</div><div class="f" style="left:176px;top:489px;width:308px"></div>
  <div class="t" style="left:51px;top:513px">Legal Next of Kin:</div><div class="f" style="left:157px;top:513px;width:326px"></div>
  <div class="t" style="left:490px;top:513px">Telephone:</div><div class="f" style="left:561px;top:513px;width:245px"></div>
  <div class="t" style="left:813px;top:513px">/</div><div class="f" style="left:824px;top:513px;width:231px"></div>
  <div class="t" style="left:51px;top:537px">Address:</div><div class="f" style="left:108px;top:537px;width:375px"></div>
  <div class="t" style="left:490px;top:537px">E-mail &nbsp;&nbsp;:</div><div class="f" style="left:562px;top:537px;width:246px"></div>
  <div class="t" style="left:51px;top:561px">Is significant other able, available, capable and willing to care for patient?</div>
  <div class="cb" style="left:563px;top:561px"></div><div class="t" style="left:599px;top:561px">Yes</div>
  <div class="cb" style="left:642px;top:561px"></div><div class="t" style="left:674px;top:561px">No</div>
  <div class="t" style="left:51px;top:586px">If No, explain:</div><div class="f" style="left:137px;top:586px;width:917px"></div>
  <div class="t" style="left:51px;top:610px">Educational Needs of Patient/Family:</div><div class="f" style="left:274px;top:610px;width:780px"></div>

  <div class="section" style="top:651px">ENVIRONMENT :</div>
  <div class="cb" style="left:51px;top:675px"></div><div class="t" style="left:73px;top:675px">Private Home</div>
  <div class="cb" style="left:231px;top:675px"></div><div class="t" style="left:253px;top:675px">Elevator</div>
  <div class="cb" style="left:385px;top:675px"></div><div class="t" style="left:407px;top:675px">Apartment</div>
  <div class="cb" style="left:562px;top:675px"></div><div class="t" style="left:584px;top:675px">Walkup</div>

  <div class="section" style="top:716px">SAFETY HAZARDS IN THE HOME:</div>
  <div class="cb" style="left:51px;top:741px"></div><div class="t" style="left:73px;top:741px">Sound structure</div>
  <div class="cb" style="left:385px;top:741px"></div><div class="t" style="left:407px;top:741px">Safe Placement of Cords, Rugs and Furniture</div>
  <div class="cb" style="left:744px;top:741px"></div><div class="t" style="left:766px;top:741px">Adequate Heating and Ventilation</div>
  <div class="cb" style="left:51px;top:765px"></div><div class="t" style="left:73px;top:765px">Adequate Cooking facility</div>
  <div class="cb" style="left:385px;top:765px"></div><div class="t" style="left:407px;top:765px">Adequate Plumbing/Sanitation/ Running Water</div>
  <div class="cb" style="left:744px;top:765px"></div><div class="t" style="left:766px;top:765px">Adequate Sleeping Arrangement</div>
  <div class="cb" style="left:51px;top:789px"></div><div class="t" style="left:73px;top:789px">Safe Gas/Electric Appliances</div>
  <div class="cb" style="left:385px;top:789px"></div><div class="t" style="left:407px;top:789px">Grounded Plug for Equipment</div>
  <div class="cb" style="left:744px;top:789px"></div><div class="t" style="left:766px;top:789px">Enough Electrical Outlets for Equipment</div>
  <div class="cb" style="left:51px;top:813px"></div><div class="t" style="left:73px;top:813px">Working Telephone in the Home</div>
  <div class="cb" style="left:385px;top:813px"></div><div class="t" style="left:407px;top:813px">Safe storage for Supplies/Equipment/Meds?</div>
  <div class="cb" style="left:744px;top:813px"></div><div class="t" style="left:766px;top:813px">Exits Free of Obstruction</div>
  <div class="cb" style="left:51px;top:837px"></div><div class="t" style="left:73px;top:837px">Working smoke detectors?</div>
  <div class="cb" style="left:385px;top:837px"></div><div class="t" style="left:407px;top:837px">Fire extinguisher in home?</div>
  <div class="cb" style="left:744px;top:837px"></div><div class="t" style="left:766px;top:837px">Infestations of pests?</div>
  <div class="cb" style="left:51px;top:861px"></div><div class="t" style="left:73px;top:861px">Neighborhood safe?</div>
  <div class="t" style="left:51px;top:885px">Comments:</div><div class="f" style="left:120px;top:885px;width:935px"></div>

  <div class="section" style="top:926px">CAREGIVER’S CONTACT INFORMATION:</div>
  <div class="t" style="left:51px;top:951px">Name</div><div class="t" style="left:193px;top:951px">:</div><div class="f" style="left:205px;top:951px;width:539px"></div>
  <div class="t" style="left:51px;top:975px">Telephone</div><div class="t" style="left:193px;top:975px">:</div><div class="f" style="left:205px;top:975px;width:181px"></div>
  <div class="t" style="left:388px;top:975px">/</div><div class="f" style="left:395px;top:975px;width:349px"></div>
  <div class="t" style="left:51px;top:999px">Address</div><div class="t" style="left:193px;top:999px">:</div><div class="f" style="left:205px;top:999px;width:275px"></div>
  <div class="t" style="left:483px;top:999px">E-mail:</div><div class="f" style="left:529px;top:999px;width:215px"></div>
  <div class="t" style="left:51px;top:1023px">Days / Time Available</div><div class="t" style="left:193px;top:1023px">:</div><div class="f" style="left:205px;top:1023px;width:540px"></div>

  <div class="section" style="top:1064px">CAREGIVERS ABILITY TO ASSIST PATIENT / ABLE TO PROVIDE:</div>
  <div class="t" style="left:51px;top:1088px">Personal Care:</div>
  <div class="cb" style="left:385px;top:1088px"></div><div class="t" style="left:407px;top:1088px">Yes</div>
  <div class="cb" style="left:445px;top:1088px"></div><div class="t" style="left:467px;top:1088px">No</div>
  <div class="t" style="left:572px;top:1088px">Maintain Safe/Clean Environment:</div>
  <div class="cb" style="left:898px;top:1088px"></div><div class="t" style="left:920px;top:1088px">Yes</div>
  <div class="cb" style="left:958px;top:1088px"></div><div class="t" style="left:980px;top:1088px">No</div>
  <div class="t" style="left:51px;top:1112px">Mobility:</div>
  <div class="cb" style="left:385px;top:1112px"></div><div class="t" style="left:407px;top:1112px">Yes</div>
  <div class="cb" style="left:445px;top:1112px"></div><div class="t" style="left:467px;top:1112px">No</div>
  <div class="t" style="left:572px;top:1112px">Perform/ Assist with Procedures:</div>
  <div class="cb" style="left:898px;top:1112px"></div><div class="t" style="left:920px;top:1112px">Yes</div>
  <div class="cb" style="left:958px;top:1112px"></div><div class="t" style="left:980px;top:1112px">No</div>
  <div class="t" style="left:51px;top:1136px">Prepare/Serve Meals:</div>
  <div class="cb" style="left:385px;top:1136px"></div><div class="t" style="left:407px;top:1136px">Yes</div>
  <div class="cb" style="left:445px;top:1136px"></div><div class="t" style="left:467px;top:1136px">No</div>
  <div class="t" style="left:572px;top:1136px">Caregiver has capacity to learn therapeutic regimen:</div>
  <div class="cb" style="left:898px;top:1136px"></div><div class="t" style="left:920px;top:1136px">Yes</div>
  <div class="cb" style="left:958px;top:1136px"></div><div class="t" style="left:980px;top:1136px">No</div>
  <div class="t" style="left:51px;top:1160px">Comments:</div><div class="f" style="left:120px;top:1160px;width:935px"></div>

  <div class="t b u" style="left:51px;top:1201px">Are There Any Signs of Abuse or Neglect from Family or Caregiver?:</div>
  <div class="cb" style="left:502px;top:1201px"></div><div class="t b u" style="left:522px;top:1201px">Yes</div>
  <div class="cb" style="left:566px;top:1201px"></div><div class="t b u" style="left:588px;top:1201px">No</div>
  <div class="t b u" style="left:51px;top:1225px">If Yes, describe:</div>
  <div class="note-box"></div>

  <div class="footer-band"></div>
</div>
</div>
</body>
</html>
```